Business Card design which attached logo. Company is called Tallowind Shield and main colours are Orange & Black.

Company specialises in Paint Protection and Detailing for supercars.

Details needed on business card:

Sales

Address: Unit 14, 172 Garrick Road, Wexley Vale, NSW 2381

Phone: 02 9461 2738

website: www.tallowindshield.com.au

Email: sales@tallowindshield.com.au

```html
<!DOCTYPE html>
<html lang="en">
<head>
<meta charset="utf-8">
<title>Tallowind Shield – Business Card</title>
<link rel="stylesheet" href="https://fonts.googleapis.com/css2?family=Lato:wght@300&family=Montserrat:wght@400;500&family=Open+Sans:wght@400&display=swap">
<style>
  :root {
    --page-bg: #e9e9e9;
    --card-white: #ffffff;
    --card-black: #06080a;
    --orange: #f15a2b;
    --ink: #3b3b3b;
  }
  * { margin: 0; padding: 0; box-sizing: border-box; }
  html, body {
    width: 1111px; height: 1200px; overflow: hidden;
    background: var(--page-bg);
  }
  .card {
    position: absolute;
    width: 724px; height: 404px;
    left: 203px;
    overflow: hidden;
  }
  .card--front { top: 142px; background: var(--card-white); }
  .card--back { top: 631px; background: var(--card-black); }

  .car-art {
    position: absolute;
    border-radius: 40% 55% 10% 10% / 60% 70% 10% 10%;
  }
  .card--front .car-art {
    left: 196px; top: 56px; width: 333px; height: 83px;
    background: linear-gradient(180deg, #fdebe4, #fbd7c9);
  }
  .card--back .car-art {
    left: 126px; top: 103px; width: 471px; height: 115px;
    background: linear-gradient(180deg, #2a140d, #3d1a0e);
  }

  .wordmark {
    position: absolute; left: 0; right: 0;
    text-align: center;
    font-family: "Lato", sans-serif; font-weight: 300;
    color: var(--orange);
    text-transform: uppercase;
    line-height: 1;
  }
  .card--front .wordmark { top: 163px; font-size: 23px; }
  .card--back .wordmark { top: 252px; font-size: 32px; }

  .identity {
    position: absolute; right: 396px; top: 243px;
    text-align: right;
    font-family: "Montserrat", sans-serif;
    line-height: 1;
  }
  .identity__name {
    font-size: 26px; font-weight: 500; color: var(--orange);
    text-transform: uppercase; white-space: nowrap;
  }
  .identity__role {
    margin-top: 6px; font-size: 20px; font-weight: 400; color: var(--ink);
  }
  .divider {
    position: absolute; left: 349px; top: 238px;
    width: 2px; height: 65px; background: var(--orange);
  }
  .contacts {
    position: absolute; left: 376px; top: 239px;
    list-style: none;
    font-family: "Open Sans", sans-serif; font-size: 17px; color: var(--ink);
  }
  .contacts li {
    display: flex; align-items: center; gap: 6px;
    height: 21.5px; white-space: nowrap;
  }
  .contacts svg { width: 12px; height: 12px; flex: none; }
  .address {
    position: absolute; left: 0; right: 0; top: 325px;
    text-align: center;
    font-family: "Open Sans", sans-serif; font-size: 17px; color: var(--ink);
  }
  .band {
    position: absolute; left: 0; right: 0; bottom: 0;
    height: 15px; background: var(--orange);
  }
</style>
</head>
<body>
  <section class="card card--front" aria-label="Business card front">
    <div class="car-art" role="img" aria-label="Line drawing of a supercar in orange"></div>
    <div class="wordmark">Tallowind Shield</div>

    <div class="identity">
      <div class="identity__name">Tallowind Shield</div>
      <div class="identity__role">Founder &amp; CEO</div>
    </div>
    <div class="divider"></div>
    <ul class="contacts">
      <li>
        <svg viewBox="0 0 12 12" aria-hidden="true"><rect x="3" y="0.8" width="6" height="10.4" rx="1.2" fill="none" stroke="#f15a2b" stroke-width="1.3"/><circle cx="6" cy="9.3" r="0.7" fill="#f15a2b"/></svg>
        02 9461 2738
      </li>
      <li>
        <svg viewBox="0 0 12 12" aria-hidden="true"><rect x="0.8" y="2.5" width="10.4" height="7.5" fill="none" stroke="#f15a2b" stroke-width="1.3"/><path d="M0.8 2.5 L6 7 L11.2 2.5" fill="none" stroke="#f15a2b" stroke-width="1.3"/></svg>
        sales@tallowindshield.com.au
      </li>
      <li>
        <svg viewBox="0 0 12 12" aria-hidden="true"><circle cx="6" cy="6" r="5" fill="none" stroke="#f15a2b" stroke-width="1.3"/><path d="M1 6 H11 M6 1 C3.5 4 3.5 8 6 11 M6 1 C8.5 4 8.5 8 6 11" fill="none" stroke="#f15a2b" stroke-width="1"/></svg>
        www.tallowindshield.com.au
      </li>
    </ul>
    <p class="address">Unit 14, 172 Garrick Road, Wexley Vale, NSW 2381</p>
    <div class="band"></div>
  </section>

  <section class="card card--back" aria-label="Business card back">
    <div class="car-art" role="img" aria-label="Line drawing of a supercar in orange on black"></div>
    <div class="wordmark">Tallowind Shield</div>
  </section>
</body>
</html>
```